Harlow Ironworks Business Card

We need a business card design for a new small metal fabrication business in rural NSW, Australia.

The business (Harlow Ironworks) is owner operated by a man with the initials KB - much of the branding comes from this name.

Harlow Ironworks designs, engineers, repairs and manufactures a range of custom, quality metal works including vehicle trays, agricultural machinery impliments, trailers, wood splitters, fire pits, furniture etc.

The brand position focuses on custom work of the highest quality.

Business card design should show quality, attention to detail and stand out among a mass of business cards.

Logos are in the files

The grey color may be changed on the logo if required to stand out more.

There is an image attached of a simple card that is liked because it is clean, clear, simple, masculine and effective. It says 'quality'. As most of the work we do is custom it would be good to have the business card speak to this.

Target Market(s)

Rural and regional based Australians. Primarily adult male 25-60 yrs. Primary production / rural / travelling lifestyle.

Industry/Entity Type

Metal Fabrication

Contact Information for Business Card

The words 'custom quality fabrications' would be great somewhere perhaps on the backside (not on the information side)
Name
title
Phone: 0418 539 746 and (02) 6193 4827
email: info@harlowiw.com.au
www.harlowiw.com.au

address (2 lines)

Requirements
Nice to have
• Background colour should be very navy blue or black.
Should not have
• NO orange and blue combinations.
• Navy is OK

```html
<!DOCTYPE html>
<html lang="en">
<head>
<meta charset="utf-8">
<title>Harlow Ironworks – Business Card</title>
<link href="https://fonts.googleapis.com/css2?family=Montserrat:wght@400;500;600;700&display=swap" rel="stylesheet">
<style>
  :root {
    --backdrop: #e9e9e7;
    --card: #ffffff;
    --green: #5cb82e;
    --grey: #8c8c8c;
    --grey-dark: #6f6f6f;
    --rule: #b9b9b9;
  }
  * { box-sizing: border-box; margin: 0; padding: 0; }
  html, body {
    width: 1200px; height: 840px; overflow: hidden;
    background: var(--backdrop);
    font-family: "Montserrat", sans-serif;
  }
  .card {
    position: absolute; left: 150px; top: 163px;
    width: 900px; height: 514px;
    background: var(--card);
    box-shadow: 0 18px 40px rgba(0,0,0,0.12);
  }
  .brand {
    position: absolute; left: 70px; top: 190px;
    display: flex; align-items: center; gap: 16px;
  }
  .brand-square { width: 22px; height: 22px; background: var(--green); flex: none; }
  .brand-name {
    color: var(--grey); font-weight: 700; font-size: 34px;
    line-height: 1.1; letter-spacing: 0.5px; text-transform: uppercase;
  }
  .divider {
    position: absolute; left: 370px; top: 150px;
    width: 1px; height: 200px; background: var(--rule);
  }
  .details { position: absolute; left: 410px; top: 142px; }
  .person-name {
    color: var(--green); font-weight: 700; font-size: 40px;
    line-height: 1; letter-spacing: 1px;
  }
  .person-title {
    color: var(--grey-dark); font-weight: 500; font-size: 28px;
    margin-top: 4px; margin-bottom: 18px;
  }
  .contact-list { list-style: none; }
  .contact-item {
    display: flex; align-items: center; gap: 14px;
    color: var(--grey-dark); font-size: 22px; line-height: 34px;
  }
  .contact-icon { width: 24px; height: 24px; flex: none; }
  .address {
    position: absolute; left: 0; right: 0; bottom: 58px;
    text-align: center; color: var(--grey); font-size: 22px; font-weight: 500;
  }
</style>
</head>
<body>
  <main class="card">
    <div class="brand">
      <span class="brand-square"></span>
      <span class="brand-name">Harlow<br>Ironworks</span>
    </div>

    <div class="divider"></div>

    <section class="details">
      <h1 class="person-name">KIERAN BLAKE</h1>
      <p class="person-title">Manager</p>
      <ul class="contact-list">
        <li class="contact-item">
          <svg class="contact-icon" viewBox="0 0 24 24" aria-hidden="true"><circle cx="12" cy="12" r="12" fill="var(--green)"/><path d="M8 7h2l1 3-1.5 1a7 7 0 0 0 3.5 3.5l1-1.5 3 1v2a1 1 0 0 1-1 1A9 9 0 0 1 7 8a1 1 0 0 1 1-1z" fill="#fff"/></svg>
          0418 539 746
        </li>
        <li class="contact-item">
          <svg class="contact-icon" viewBox="0 0 24 24" aria-hidden="true"><circle cx="12" cy="12" r="12" fill="var(--green)"/><rect x="6" y="9" width="12" height="8" rx="1.5" fill="#fff"/><path d="M6 9a6 3 0 0 1 12 0" stroke="#fff" stroke-width="2" fill="none"/><circle cx="12" cy="13" r="1.8" fill="var(--green)"/></svg>
          (02) 6193 4827
        </li>
        <li class="contact-item">
          <svg class="contact-icon" viewBox="0 0 24 24" aria-hidden="true"><circle cx="12" cy="12" r="12" fill="var(--green)"/><rect x="6" y="8" width="12" height="8.5" rx="1" fill="#fff"/><path d="M6.5 8.5 12 13l5.5-4.5" stroke="var(--green)" stroke-width="1.3" fill="none"/></svg>
          info@harlowiw.com.au
        </li>
        <li class="contact-item">
          <svg class="contact-icon" viewBox="0 0 24 24" aria-hidden="true"><circle cx="12" cy="12" r="12" fill="var(--green)"/><g stroke="#fff" stroke-width="1.3" fill="none"><circle cx="12" cy="12" r="6"/><ellipse cx="12" cy="12" rx="2.6" ry="6"/><path d="M6 12h12M7 9h10M7 15h10"/></g></svg>
          www.harlowiw.com.au
        </li>
      </ul>
    </section>

    <p class="address">48 Quarry Road, Tumut, NSW 2720</p>
  </main>
</body>
</html>
```